Home Remodeling company needs a business card design

we need a business card design for home remodeling company in hamilton county, indiana USA. we offers a wide range of construction services including whole house renovations, Design and Build Basements and Kitchen and Bathroom Remodeling . we would like to see designs for both site of business card that use the same color of the company logo and also including all information below :
1- Tarek Salim CEO / General Contractor
2- all company contacts Telephone numbers ( 1-888-VOLMI-15 ) ( 317-555-0192) email address ( info@volmihome.example) website ( www.volmihome.example ) and social media logos (Facebook- twitter- google plus )
3- company logo
4- licensed . insured . bonded

```html
<!DOCTYPE html>
<html lang="en">
<head>
<meta charset="utf-8">
<title>Volmi Home Remodeling – Business Card</title>
<link href="https://fonts.googleapis.com/css2?family=Roboto:wght@400;700&display=swap" rel="stylesheet">
<style>
  :root {
    --backdrop: #3b322e;
    --card-black: #141414;
    --card-black-soft: #222223;
    --gloss: #2c2c2c;
    --brand-red: #e02a22;
    --ink-white: #f2f2f2;
    --ink-grey: #cfcfcf;
    --band-white: #ececec;
    --rule: #8a8a8a;
  }
  * { box-sizing: border-box; margin: 0; padding: 0; }
  html, body {
    width: 1200px; height: 716px; overflow: hidden;
    background: var(--backdrop);
    font-family: "Roboto", Arial, sans-serif;
  }
  .stage {
    position: relative; width: 1200px; height: 716px;
    display: flex; align-items: center; justify-content: center; gap: 60px;
  }
  .card {
    position: relative; width: 510px; height: 292px; overflow: hidden;
    border-radius: 3px;
    box-shadow: 0 14px 30px rgba(0,0,0,.45);
  }
  /* Front */
  .card--front {
    background: var(--card-black);
    display: flex; align-items: center; justify-content: center;
  }
  .brand {
    display: flex; align-items: center; gap: 12px;
    font-weight: 700; letter-spacing: 3px; text-transform: uppercase;
  }
  .brand__mark { width: 12px; height: 12px; }
  .card--front .brand { color: var(--gloss); font-size: 34px; }
  .card--front .brand__mark { background: var(--gloss); width: 14px; height: 14px; }
  .card--front .brand__sub { font-size: 15px; letter-spacing: 6px; display: block; margin-top: 4px; }

  /* Back */
  .card--back {
    background: radial-gradient(ellipse at 40% 30%, var(--card-black-soft), var(--card-black) 75%);
    color: var(--ink-white);
  }
  .card--back .brand {
    position: absolute; top: 26px; left: 96px;
    color: var(--ink-white); font-size: 34px;
  }
  .card--back .brand__mark { background: var(--brand-red); }
  .card--back .brand__sub { font-size: 14px; letter-spacing: 6px; display: block; margin-top: 4px; }

  .person { position: absolute; top: 112px; left: 26px; }
  .person__name { color: var(--brand-red); font-size: 17px; font-weight: 700; }
  .person__title { color: var(--ink-grey); font-size: 10.5px; margin-top: 3px; }
  .social { position: absolute; top: 166px; left: 26px; display: flex; gap: 4px; }
  .social__tile { width: 15px; height: 15px; background: var(--ink-grey); border-radius: 2px; }

  .contacts { position: absolute; top: 128px; left: 288px; list-style: none; }
  .contacts__item { display: flex; align-items: center; gap: 9px; font-size: 12px; line-height: 17px; }
  .contacts__icon { width: 10px; height: 10px; flex: none; }
  .credentials {
    position: absolute; top: 208px; left: 282px; width: 200px;
    border-top: 1px solid var(--rule); padding-top: 6px;
    font-size: 12px; color: var(--ink-white); text-align: center; letter-spacing: .3px;
  }
  .bottom-bands { position: absolute; left: 0; bottom: 0; width: 510px; height: 70px; }
</style>
</head>
<body>
<main class="stage">

  <section class="card card--front" aria-label="Card front">
    <div class="brand">
      <span class="brand__mark"></span>
      <span>Volmi<span class="brand__sub">Home Remodeling</span></span>
    </div>
  </section>

  <section class="card card--back" aria-label="Card back">
    <div class="brand">
      <span class="brand__mark"></span>
      <span>Volmi<span class="brand__sub">Home Remodeling</span></span>
    </div>

    <div class="person">
      <p class="person__name">Tarek Salim</p>
      <p class="person__title">CEO / General Contractor</p>
    </div>

    <div class="social" aria-label="Social media">
      <span class="social__tile"></span>
      <span class="social__tile"></span>
      <span class="social__tile"></span>
    </div>

    <ul class="contacts">
      <li class="contacts__item">
        <svg class="contacts__icon" viewBox="0 0 10 10"><path d="M2 1 L4 1 L4.6 3 L3.5 4 Q4.5 6 6 6.5 L7 5.4 L9 6 L9 8 Q5 9 1.5 5 Q1 3 2 1Z" fill="var(--brand-red)"/></svg>
        1-888-VOLMI-15</li>
      <li class="contacts__item">
        <svg class="contacts__icon" viewBox="0 0 10 10"><rect x="1" y="3" width="8" height="6" rx="1" fill="var(--brand-red)"/><rect x="3" y="1" width="4" height="3" fill="var(--brand-red)"/></svg>
        317-555-0192</li>
      <li class="contacts__item">
        <svg class="contacts__icon" viewBox="0 0 10 10"><rect x="0.5" y="2" width="9" height="6" fill="var(--brand-red)"/><path d="M0.5 2 L5 5.5 L9.5 2" stroke="#141414" fill="none"/></svg>
        info@volmihome.example</li>
      <li class="contacts__item">
        <svg class="contacts__icon" viewBox="0 0 10 10"><circle cx="5" cy="5" r="4.5" fill="var(--brand-red)"/><path d="M0.5 5 H9.5 M5 0.5 V9.5" stroke="#141414" stroke-width=".8"/></svg>
        www.volmihome.example</li>
    </ul>

    <p class="credentials">Licensed &nbsp;•&nbsp; Insured &nbsp;•&nbsp; Bonded</p>

    <svg class="bottom-bands" viewBox="0 0 510 70" preserveAspectRatio="none" aria-hidden="true">
      <polygon points="0,8 0,70 510,70 510,64 360,64 330,48 0,8" fill="var(--band-white)"/>
      <polygon points="300,58 330,48 360,64 510,64 510,70 310,70" fill="var(--brand-red)"/>
      <polygon points="0,8 330,48 300,58 0,22" fill="#1b1b1b"/>
    </svg>
  </section>

</main>
</body>
</html>
```